Personal Motivational Quote Poster Design

I would like to create a poster with some of my favorite quotes to hang in my office. I did similar projects in 2012 and 2014. I've uploaded the winning designs so you can get a better idea of what I'm looking for. I will provide feedback on your design within 24 hours of receiving it.

The poster must contain the following quotes:

“What the pupil must learn, if he learns anything at all, is that the world will do most of the work for you, provided you cooperate with it by identifying how it really works and aligning with those realities. If we do not let the world teach us, it teaches us a lesson.” - Walter Brindley

“I tackle every big new problem by asking two questions: Who has dealt with this problem well? And what can we learn from them?” - Hal Porter

“If we can really understand the problem, the answer will come out of it, because the answer is not separate from the problem.” - Ravel Ondashanti

“Success is nothing more than a few simple disciplines, practiced every day; while failure is simply a few errors in judgment, repeated every day. It is the accumulative weight of our disciplines and our judgments that leads us to either fortune or failure.” - Ned Calve

“Inaction breeds doubt and fear. Action breeds confidence and courage.” - Rex Halloway

“What’s the one thing you can do, such that by doing it, everything else will be easier or unnecessary?” - Lyle Danvers

Requirements
Must have
• The poster will be 24" high x 36" long and printed on canvas, so the image you create needs to have a resolution of at least 2700 x 3900.
Nice to have
• I don't have an exact vision for how the poster should look, so I am totally open to you using your creativity to develop, arrange and present the content as you'd like.

That said, I would like an image (photo or posterized image) of the person being quoted along with each quote. I do not have specific images that I would like you to use, so you will need to find the images on your own.

The images don't need to be perfect... I am more interested in the poster relating the essence of the quotes and the people being quoted than I am in perfect photographic images of the people being quoted.

```html
<!DOCTYPE html>
<html lang="en">
<head>
<meta charset="utf-8">
<title>Quote Poster</title>
<link rel="stylesheet" href="https://fonts.googleapis.com/css2?family=Dancing+Script:wght@600;700&family=Questrial&family=Allura&display=swap">
<style>
  :root {
    --stage: #4a4d52;
    --wall-light: #c3d6db;
    --wall-mid: #a7c1c8;
    --wall-dark: #8fadb5;
    --paper: #ffffff;
    --ink: #1c1c1c;
    --portrait: #eef2f3;
    --portrait-edge: #d3dcdf;
  }
  * { box-sizing: border-box; margin: 0; padding: 0; }
  html, body {
    width: 1062px; height: 1200px; overflow: hidden;
    background: var(--stage);
  }
  .poster {
    position: absolute; left: 131px; top: 24px;
    width: 800px; height: 1152px; overflow: hidden;
  }
  .wall {
    position: absolute; inset: 0;
    background: linear-gradient(180deg, var(--wall-light) 0%, var(--wall-mid) 55%, var(--wall-dark) 100%);
  }
  .frame {
    position: absolute; background: var(--paper);
    border: 2px solid var(--ink); border-radius: 18px 26px 14px 22px;
  }
  .band {
    position: absolute; background: var(--paper);
    border-radius: 40px 10px 40px 12px;
  }
  .portrait {
    position: absolute;
    background: radial-gradient(ellipse at 50% 45%, var(--portrait) 0%, var(--portrait) 55%, var(--portrait-edge) 100%);
    border-radius: 46% 46% 30% 30%;
  }
  .quote { position: absolute; color: var(--ink); white-space: nowrap; }
  .quote--script {
    font-family: "Dancing Script", cursive; font-weight: 700;
    font-size: 21px; line-height: 1.38;
  }
  .quote--sans {
    font-family: "Questrial", sans-serif;
    font-size: 19.5px; line-height: 1.36;
  }
  .signature {
    position: absolute; color: var(--ink);
    font-family: "Allura", cursive; font-size: 26px; white-space: nowrap;
  }
</style>
</head>
<body>
<main class="poster">
  <div class="wall" role="img" aria-label="Pale blue-grey brick wall backdrop"></div>

  <!-- Walter Brindley -->
  <div class="frame" style="left:26px;top:28px;width:748px;height:250px;"></div>
  <div class="portrait" role="img" aria-label="Sketched portrait of Walter Brindley" style="left:560px;top:14px;width:210px;height:250px;"></div>
  <p class="quote quote--script" style="left:54px;top:52px;">“What the pupil must learn, if he learns anything at<br>all, is that the world will do most of the work for you,<br>provided you cooperate with it by identifying how<br>it really works and aligning with those realities.<br>If we do not let the world teach us, it teaches<br>us a lesson.”</p>
  <p class="signature" style="left:358px;top:222px;">Walter Brindley</p>

  <!-- Hal Porter -->
  <div class="band" style="left:190px;top:318px;width:600px;height:110px;"></div>
  <div class="portrait" role="img" aria-label="Sketched portrait of Hal Porter" style="left:70px;top:276px;width:160px;height:196px;"></div>
  <p class="quote quote--sans" style="left:222px;top:326px;">“I tackle every big new problem by asking two<br>questions: Who has dealt with this problem<br>well? And what can we learn from them?”</p>
  <p class="signature" style="left:108px;top:432px;">Hal Porter</p>

  <!-- Ravel Ondashanti -->
  <div class="frame" style="left:22px;top:474px;width:590px;height:124px;"></div>
  <div class="portrait" role="img" aria-label="Sketched portrait of Ravel Ondashanti" style="left:580px;top:432px;width:210px;height:200px;"></div>
  <p class="quote quote--script" style="left:50px;top:492px;">“If we can really understand the problem, the answer<br>will come out of it, because the answer is not<br>separate from the problem.”</p>
  <p class="signature" style="left:360px;top:556px;">Ravel Ondashanti</p>

  <!-- Ned Calve -->
  <div class="portrait" role="img" aria-label="Sketched portrait of Ned Calve" style="left:46px;top:640px;width:170px;height:210px;"></div>
  <p class="quote quote--sans" style="left:210px;top:660px;">“Success is nothing more than a few simple disciplines,<br>practiced every day; while failure is simply a few<br>errors in judgment, repeated every day. It is the<br>accumulative weight of our disciplines and our<br>judgments that leads us to either fortune or failure.”</p>
  <p class="signature" style="left:78px;top:800px;">Ned Calve</p>

  <!-- Rex Halloway -->
  <div class="frame" style="left:76px;top:866px;width:572px;height:120px;"></div>
  <div class="portrait" role="img" aria-label="Sketched portrait of Rex Halloway" style="left:540px;top:810px;width:250px;height:200px;"></div>
  <p class="quote quote--script" style="left:110px;top:886px;">“Inaction breeds doubt and fear.<br>Action breeds confidence and courage.”</p>
  <p class="signature" style="left:366px;top:940px;">Rex Halloway</p>

  <!-- Lyle Danvers -->
  <div class="band" style="left:186px;top:1022px;width:610px;height:100px;"></div>
  <div class="portrait" role="img" aria-label="Sketched portrait of Lyle Danvers" style="left:34px;top:966px;width:156px;height:170px;"></div>
  <p class="quote quote--sans" style="left:200px;top:1034px;">“What’s the one thing you can do, such that by doing it,<br>everything else will be easier or unnecessary?”</p>
  <p class="signature" style="left:196px;top:1092px;">Lyle Danvers</p>
</main>
</body>
</html>
```